Gardener needs an exciting new flyer design.

I'm a passionate gardener that requires a custom flyer design for a owner operator gardening business. Design will be for a DL flyer. I'm based on the Sunshine coast in Queensland Australia. My target audience is the residential market on the Sunshine coast. Business name is Marlowe Greens. My services are, lawn mowing, weeding, Eco Friendly fertilizing, green waste removal, Mulching, tree and shrub pruning, Full garden makeovers, hedging, pressure cleaning, privacy screening, Timber deck rejuvenation, Planting, Turf preparation and installation, and much more. Free no obligation quotes, reliable and friendly service, great rates. 12 years experience. Web www.marlowegreens.com.au - Phone 0418527064 - Email doug@marlowegreens.com.au I would like the design to portray a friendly and professional approach.

Target Market(s)

Residential

Industry/Entity Type

Gardener

Font styles to use
Serif

Colors
9ccb3b
abd037
3176b5

Requirements
Must have
• my services, my logo, my contact details,

```html
<!DOCTYPE html>
<html lang="en">
<head>
<meta charset="utf-8">
<title>Marlowe Greens – DL Flyer</title>
<link href="https://fonts.googleapis.com/css2?family=Open+Sans:ital,wght@0,400;0,600;0,700;0,800;1,800&display=swap" rel="stylesheet">
<style>
  :root {
    --forest: #1f5a25;
    --forest-deep: #173f1a;
    --moss: #4c7a4f;
    --leaf: #9ccb3b;
    --lime: #abd037;
    --blue: #3176b5;
    --paper: #ffffff;
    --ground: #e9ebe8;
    --ink-green: #3e9b3c;
  }
  * { box-sizing: border-box; margin: 0; padding: 0; }
  html, body { width: 1200px; height: 844px; overflow: hidden; }
  body {
    background: var(--ground);
    font-family: "Open Sans", Arial, sans-serif;
    position: relative;
  }
  .flyer {
    position: absolute;
    top: 40px;
    width: 360px;
    height: 764px;
    overflow: hidden;
    box-shadow: 0 6px 18px rgba(0,0,0,0.18);
  }
  .flyer--front { left: 200px; background: var(--forest); }
  .flyer--back { left: 640px; background: var(--moss); }

  /* Brand name block */
  .brand {
    display: flex; align-items: center; justify-content: center; gap: 10px;
    font-weight: 700; font-size: 30px; letter-spacing: 0.5px;
  }
  .brand__dot { width: 16px; height: 16px; border-radius: 50%; }

  /* Front */
  .front__head {
    position: absolute; inset: 0 0 auto 0; height: 160px;
    background: var(--paper);
    display: flex; align-items: flex-end; justify-content: center; padding-bottom: 28px;
  }
  .front__head .brand { color: var(--ink-green); }
  .front__head .brand__dot { background: var(--ink-green); }
  .front__hero {
    position: absolute; left: 0; right: 0; top: 160px; height: 180px;
    background: linear-gradient(180deg, #dfe6df 0%, #4f7f3c 30%, #2f6a27 60%, #7fb33e 78%, #5fa02e 100%);
  }
  .front__body {
    position: absolute; left: 0; top: 340px; width: 360px; height: 280px;
    background: var(--forest);
  }
  .front__intro {
    position: absolute; left: 22px; top: 356px; width: 178px;
    color: var(--paper); font-size: 11.5px; line-height: 1.32;
  }
  .front__intro p + p { margin-top: 12px; }
  .front__path {
    position: absolute; left: 212px; top: 372px; width: 148px; height: 260px;
    background: linear-gradient(180deg, #2d5a2a 0%, #5b7f4e 40%, #9b86c4 70%, #c7b9d9 100%);
  }
  .front__foot {
    position: absolute; left: 0; right: 0; bottom: 0; height: 132px;
    background: var(--forest-deep);
  }
  .badge {
    position: absolute; left: 156px; top: 588px; width: 96px; height: 96px;
    border-radius: 50%; background: var(--blue); border: 5px solid #4a3a73;
    color: var(--paper); text-align: center; font-weight: 800;
    display: flex; flex-direction: column; justify-content: center; line-height: 1;
  }
  .badge__num { font-size: 30px; }
  .badge__label { font-size: 11px; margin-top: 2px; }
  .badge__ribbon {
    display: block; background: #3a95d6; margin: 4px -18px 0; padding: 3px 0; font-size: 10px;
  }

  .contact { position: absolute; left: 0; right: 0; color: var(--paper); text-align: center; }
  .contact__phone {
    display: flex; align-items: center; justify-content: center; gap: 6px;
    font-weight: 800; font-size: 27px; letter-spacing: 1px;
  }
  .contact__web {
    display: flex; align-items: center; justify-content: center; gap: 6px;
    font-size: 15px; margin-top: 6px;
  }
  .front__foot .contact { top: 40px; }

  /* Back */
  .back__head {
    position: absolute; inset: 0 0 auto 0; height: 260px; background: var(--moss);
    display: flex; align-items: center; justify-content: center;
  }
  .back__head .brand { color: var(--paper); }
  .back__head .brand__dot { background: var(--paper); }
  .back__panel {
    position: absolute; left: 0; right: 0; top: 260px; height: 380px;
    background: linear-gradient(180deg, #8fc850 0%, #7cbd3a 55%, #5fa52a 100%);
  }
  .back__grass {
    position: absolute; left: 0; right: 0; top: 440px; height: 210px;
    background: linear-gradient(180deg, rgba(156,203,59,0) 0%, #4f9a22 45%, #2f7a1c 100%);
  }
  .services {
    position: absolute; left: 0; right: 0; top: 282px; text-align: center;
    color: var(--paper);
  }
  .services__title {
    color: #2f7a3a; font-weight: 800; font-size: 24px; letter-spacing: 1px; margin-bottom: 6px;
  }
  .services__list { list-style: none; font-size: 14px; line-height: 1.3; }
  .back__foot {
    position: absolute; left: 0; right: 0; bottom: 0; height: 130px; background: var(--forest-deep);
  }
  .tagline {
    position: absolute; left: 0; right: 0; top: 14px; text-align: center;
    color: var(--paper); font-weight: 800; font-style: italic; font-size: 14px;
    line-height: 1.2; text-transform: uppercase;
  }
  .back__foot .contact { top: 58px; }
</style>
</head>
<body>

<section class="flyer flyer--front" aria-label="Flyer front">
  <header class="front__head">
    <div class="brand"><span class="brand__dot"></span>Marlowe Greens</div>
  </header>
  <div class="front__hero" role="img" aria-label="Photo of a landscaped garden with lawn, flower beds and trees"></div>
  <div class="front__body"></div>
  <div class="front__intro">
    <p>Marlowe Greens is your garden and lawn care specialist, with a passion for gardening and a keen eye for detail you can rest assured you're in the right hands.</p>
    <p>My services are tailored to meet every individual clients needs.</p>
    <p>From a one time mow too regular lawn mowing, all aspects of garden care and even full garden makeovers.</p>
  </div>
  <div class="front__foot">
    <div class="contact">
      <div class="contact__phone">
        <svg width="16" height="22" viewBox="0 0 16 22" aria-hidden="true"><path d="M4 1 L8 5 L6 8 Q6 13 9 15 L12 13 L15 17 L12 21 Q2 18 1 5 Z" fill="var(--leaf)"/></svg>
        0418527064
      </div>
      <div class="contact__web">
        <svg width="14" height="14" viewBox="0 0 14 14" aria-hidden="true"><g fill="none" stroke="var(--leaf)" stroke-width="1.3"><circle cx="7" cy="7" r="6"/><ellipse cx="7" cy="7" rx="2.6" ry="6"/><path d="M1 7h12"/></g></svg>
        www.marlowegreens.com.au
      </div>
    </div>
  </div>
  <div class="front__path" role="img" aria-label="Photo of a stone garden path lined with purple flowering plants"></div>
  <div class="badge" aria-label="12 years experience">
    <span class="badge__num">12</span>
    <span class="badge__label">YEARS</span>
    <span class="badge__ribbon">EXPERIENCE</span>
  </div>
</section>

<section class="flyer flyer--back" aria-label="Flyer back">
  <header class="back__head">
    <div class="brand"><span class="brand__dot"></span>Marlowe Greens</div>
  </header>
  <div class="back__panel"></div>
  <div class="back__grass" role="img" aria-label="Close-up photo of fresh green grass"></div>
  <div class="services">
    <h2 class="services__title">SERVICES</h2>
    <ul class="services__list">
      <li>Lawn mowing,</li>
      <li>Weeding,</li>
      <li>Eco Friendly fertilizing,</li>
      <li>Green waste removal,</li>
      <li>Mulching,</li>
      <li>Tree and shrub pruning,</li>
      <li>Full garden makeovers,</li>
      <li>Hedging,</li>
      <li>Pressure cleaning,</li>
      <li>Privacy screening,</li>
      <li>Timber deck rejuvenation,</li>
      <li>Planting,</li>
      <li>Turf preparation and installation,</li>
      <li>and much more.</li>
    </ul>
  </div>
  <div class="back__foot">
    <p class="tagline">Transform your garden today<br>into a masterpiece you'll be proud of.</p>
    <div class="contact">
      <div class="contact__phone">
        <svg width="16" height="22" viewBox="0 0 16 22" aria-hidden="true"><path d="M4 1 L8 5 L6 8 Q6 13 9 15 L12 13 L15 17 L12 21 Q2 18 1 5 Z" fill="var(--leaf)"/></svg>
        0418527064
      </div>
      <div class="contact__web">
        <svg width="14" height="14" viewBox="0 0 14 14" aria-hidden="true"><g fill="none" stroke="var(--leaf)" stroke-width="1.3"><circle cx="7" cy="7" r="6"/><ellipse cx="7" cy="7" rx="2.6" ry="6"/><path d="M1 7h12"/></g></svg>
        www.marlowegreens.com.au
      </div>
    </div>
  </div>
</section>

</body>
</html>
```